Banner 170x60 for Barrel Sauna Rental Banner

Attention, please do every side graphic distance 5cm . It is for attachment.
search for a graphic design in dimension 170x60cm.
we have a barrel sauna rental service and need a banner for the two sides.
please look photos.
big text is: (I CAN RENT ME!!! )in english like: you can rent me
deine-dampfstube.de
015243719028
info@deine-dampfstube.de
we need an eye catcher design!!!!
Design:
maybe wood in at background.
maybe burning fire and sauna style.
Please don't use my barrell sauna pictures. It is only an example for you what we do. The barrel sauna is on build at the moment.

```html
<!DOCTYPE html>
<html lang="de">
<head>
<meta charset="utf-8">
<title>Deine Dampfstube – Banner</title>
<link rel="stylesheet" href="https://fonts.googleapis.com/css2?family=Anton&family=Poppins:wght@800&display=swap">
<style>
  :root {
    --canvas-grey: #c3c3c3;
    --wood-dark: #3a1208;
    --wood-mid: #6b2a14;
    --wood-light: #8a3f20;
    --plank-line: #1e0603;
    --board-light: #f5d3a0;
    --board-mid: #e4a36a;
    --board-edge: #2a0d06;
    --headline: #2a0b04;
    --headline-warm: #5c1a07;
    --band-red: #e8320f;
    --band-orange: #ff8a10;
    --band-yellow: #fff21a;
    --contact-ink: #160603;
    --brand-ink: #b78b64;
    --flame-red: rgba(235, 55, 10, 0.85);
    --flame-orange: rgba(255, 140, 20, 0.8);
    --flame-yellow: rgba(255, 225, 70, 0.75);
  }
  html, body {
    margin: 0;
    width: 1200px;
    height: 481px;
    overflow: hidden;
    background: var(--canvas-grey);
  }
  .banner {
    position: absolute;
    left: 108px;
    top: 67px;
    width: 985px;
    height: 348px;
    overflow: hidden;
    background: linear-gradient(180deg, var(--wood-dark) 0%, var(--wood-light) 35%, var(--wood-mid) 70%, var(--wood-dark) 100%);
  }
  .wood-texture {
    position: absolute;
    inset: 0;
    background:
      radial-gradient(ellipse 40% 30% at 55% 30%, rgba(200, 120, 70, 0.35), transparent 70%),
      linear-gradient(90deg, rgba(20, 4, 2, 0.35), transparent 20%, transparent 80%, rgba(20, 4, 2, 0.35));
  }
  .plank-lines {
    position: absolute;
    inset: 0;
  }
  .flames {
    position: absolute;
    inset: 0;
    background:
      radial-gradient(ellipse 14% 45% at 93% 30%, var(--flame-red), transparent 70%),
      radial-gradient(ellipse 8% 30% at 55% 25%, var(--flame-orange), transparent 70%),
      radial-gradient(ellipse 6% 25% at 77% 55%, var(--flame-orange), transparent 70%),
      radial-gradient(ellipse 12% 30% at 10% 85%, var(--flame-red), transparent 70%),
      radial-gradient(ellipse 60% 28% at 50% 100%, var(--flame-yellow), transparent 75%),
      radial-gradient(ellipse 90% 35% at 50% 100%, var(--flame-red), transparent 80%);
  }
  .brand-name {
    position: absolute;
    left: 26px;
    top: 86px;
    margin: 0;
    font-family: "Poppins", sans-serif;
    font-weight: 800;
    font-size: 16px;
    letter-spacing: 0.5px;
    color: var(--brand-ink);
  }
  .sign-board {
    position: absolute;
    left: 59px;
    top: 135px;
    width: 852px;
    height: 132px;
    border-radius: 6px;
    background:
      radial-gradient(ellipse 45% 60% at 50% 25%, var(--board-light), transparent 80%),
      linear-gradient(180deg, var(--board-mid), #d48550);
    box-shadow: 8px 6px 0 var(--board-edge), -3px 3px 0 var(--board-edge);
  }
  .headline {
    position: absolute;
    left: 0;
    right: 0;
    top: 0;
    bottom: 0;
    margin: 0;
    display: flex;
    align-items: center;
    justify-content: center;
    font-family: "Anton", sans-serif;
    font-weight: 400;
    font-size: 84px;
    line-height: 1;
    letter-spacing: 1px;
    background: linear-gradient(90deg, var(--headline) 0%, var(--headline-warm) 50%, var(--headline) 100%);
    -webkit-background-clip: text;
    background-clip: text;
    color: transparent;
  }
  .contact-band {
    position: absolute;
    left: 0;
    top: 285px;
    width: 100%;
    height: 41px;
    background: linear-gradient(90deg, var(--band-red) 0%, var(--band-orange) 40%, var(--band-yellow) 75%, var(--band-yellow) 100%);
    display: flex;
    align-items: center;
    justify-content: center;
    gap: 8px;
    font-family: "Poppins", sans-serif;
    font-weight: 800;
    font-size: 25px;
    color: var(--contact-ink);
    border-bottom: 3px solid var(--band-orange);
  }
  .contact-band .divider {
    width: 2px;
    height: 24px;
    background: var(--contact-ink);
  }
</style>
</head>
<body>
  <section class="banner">
    <div class="wood-texture" role="img" aria-label="Dark red wooden plank wall background"></div>
    <svg class="plank-lines" width="985" height="348" viewBox="0 0 985 348">
      <g stroke="var(--plank-line)" stroke-width="2" opacity="0.8">
        <line x1="0" y1="13" x2="985" y2="13"/>
        <line x1="0" y1="89" x2="985" y2="89"/>
        <line x1="0" y1="164" x2="985" y2="164"/>
        <line x1="0" y1="241" x2="985" y2="241"/>
      </g>
    </svg>
    <div class="flames" role="img" aria-label="Burning flames rising over the wood planks"></div>
    <p class="brand-name">DEINE-DAMPFSTUBE.DE</p>
    <div class="sign-board" role="img" aria-label="Light wooden sign board">
      <h1 class="headline">MICH KANN MAN MIETEN!!!</h1>
    </div>
    <div class="contact-band">
      <span class="contact-web">deine-dampfstube.de</span>
      <span class="divider"></span>
      <span class="contact-phone">015243719028</span>
      <span class="divider"></span>
      <span class="contact-mail">info@deine-dampfstube.de</span>
    </div>
  </section>
</body>
</html>
```